Web tool bar Project

I'm open to paying more if the quality of the bar is very good... if you feel the scope of the project does not match budget..... please quote me.

I need someone to re-design my web tool bar.

In the first attachment you can see a black tool bar (fig1). This is my old design. I want this to be the template as it shows what the text will say and where the buttons will be placed.

For the new tool bar:
-I would like the it to be white in colour (like fig.2)
-I would like the buttons to also be white. But the buttons must stand out so the designer should use the right shading to make the buttons stand out.
-The bar needs to be the quality of the bar in fig.2 (very good quality). I have had many designs done for this but no designer seems to be good enough to get the right quality.
-The text in the white boxes on the new bar should be the colours shown above the buttons next to fig.1 (blue, green, red, yellow, purple & orange).

Finally please put the logo attached (QT) at the end of the bar on the right where it says logo. The logo should blend in well with the bar as it has white in it also.

Please take note of fig.2 it is good quality with sharp edges I would like the same quality.

Any further questions please ask?

Requirements
Must have
• Quality!

```html
<!DOCTYPE html>
<html lang="en">
<head>
<meta charset="utf-8">
<title>Quiet Terrace Toolbar</title>
<link href="https://fonts.googleapis.com/css2?family=Arimo:wght@700&display=swap" rel="stylesheet">
<style>
  :root {
    --page: #ffffff;
    --bar-top: #fbfbfb;
    --bar-bottom: #e4e4e4;
    --bar-edge: #ececec;
    --btn-top: #ffffff;
    --btn-bottom: #ededed;
    --btn-shadow: rgba(0,0,0,0.32);
    --blue: #1c9ad8;
    --green: #1fdc25;
    --red: #d91b1b;
    --tan: #9e8a72;
    --purple: #c31cbc;
    --orange: #f28a12;
    --divider: #d2d2d2;
  }
  * { margin: 0; padding: 0; box-sizing: border-box; }
  html, body { width: 1200px; height: 267px; overflow: hidden; background: var(--page); }
  body { position: relative; font-family: "Arimo", Arial, sans-serif; font-weight: 700; }

  .toolbar {
    position: absolute; left: 27px; top: 92px; width: 1068px; height: 46px;
    background: linear-gradient(to bottom, var(--bar-top) 0%, #f3f3f3 45%, var(--bar-bottom) 100%);
    border-top: 2px solid var(--bar-edge);
  }
  .toolbar-end {
    position: absolute; right: 0; top: 0; width: 2px; height: 100%;
    background: linear-gradient(to right, #d6d6d6, #f7f7f7);
  }

  .button {
    position: absolute; height: 23px;
    display: flex; align-items: center; gap: 5px; padding: 0 8px;
    background: linear-gradient(to bottom, var(--btn-top), var(--btn-bottom));
    border-radius: 2px;
    box-shadow: 2px 3px 4px var(--btn-shadow);
    font-size: 8px; white-space: nowrap;
  }
  .button svg { flex: none; }

  .login   { left: 89px;  top: 12px; width: 107px; color: var(--blue); }
  .status  { left: 546px; top: 11px; width: 173px; padding: 0 4px; gap: 0; }
  .status .part { display: flex; align-items: center; gap: 3px; height: 100%; }
  .status .check  { color: var(--green); padding-right: 5px; border-right: 1px solid var(--divider); }
  .status .online { color: var(--red); padding-left: 4px; }
  .feeds   { left: 732px; top: 12px; width: 86px; color: var(--tan); gap: 8px; }
  .messages{ left: 831px; top: 12px; width: 73px; color: var(--purple); }
  .scrap   { left: 913px; top: 12px; width: 71px; color: var(--orange); padding: 0 4px; }

  .brand {
    position: absolute; left: 1019px; top: 10px; width: 32px; height: 32px;
    background: var(--blue); border-radius: 3px;
    display: flex; align-items: center; justify-content: center;
    color: #ffffff; font-size: 12px;
  }
</style>
</head>
<body>
  <nav class="toolbar">
    <span class="toolbar-end"></span>

    <a class="button login">
      <svg width="12" height="11" viewBox="0 0 12 11"><circle cx="4.5" cy="3" r="2.6" fill="var(--blue)"/><path d="M0 11c0-3.5 2-5 4.5-5S9 7.5 9 11z" fill="var(--blue)"/><circle cx="9.5" cy="6.5" r="1.8" fill="var(--blue)"/></svg>
      Quiet Terrace Login
    </a>

    <div class="button status">
      <span class="part check">
        <svg width="9" height="9" viewBox="0 0 9 9"><rect x="0.8" y="1.8" width="6.4" height="6.4" fill="none" stroke="var(--green)" stroke-width="1.6"/><path d="M3 4.5l1.5 1.5L8.5 1" fill="none" stroke="var(--green)" stroke-width="1.6"/></svg>
        Check - In
      </span>
      <span class="part online">
        <svg width="8" height="10" viewBox="0 0 8 10"><circle cx="4" cy="2.6" r="2.4" fill="var(--red)"/><path d="M0 10c0-3.4 1.6-4.8 4-4.8S8 6.6 8 10z" fill="var(--red)"/></svg>
        Online Friends at Linkory
      </span>
    </div>

    <a class="button feeds">
      <svg width="12" height="12" viewBox="0 0 12 12"><circle cx="2" cy="10" r="1.7" fill="var(--tan)"/><path d="M0.5 5.2a6.3 6.3 0 0 1 6.3 6.3" fill="none" stroke="var(--tan)" stroke-width="1.8"/><path d="M0.5 1a10.5 10.5 0 0 1 10.5 10.5" fill="none" stroke="var(--tan)" stroke-width="1.8"/></svg>
      Terrace Feeds
    </a>

    <a class="button messages">
      <svg width="12" height="9" viewBox="0 0 12 9"><rect width="12" height="9" rx="1" fill="var(--purple)"/><path d="M0.5 0.8L6 5l5.5-4.2" fill="none" stroke="#f3c8f1" stroke-width="1"/></svg>
      Messages
    </a>

    <a class="button scrap">
      <svg width="18" height="11" viewBox="0 0 18 11"><path d="M1 5.5L9 2l8 3.5-8 3.5z" fill="var(--orange)"/><path d="M1 6.5v1.3L9 11l8-3.2V6.5L9 9.8z" fill="#c86a06"/></svg>
      Scrapbook
    </a>

    <div class="brand">QT</div>
  </nav>
</body>
</html>
```